Website images and banners needed to be created

We have a website we have not used in a few months that need updated sales banners and images resized for our web devs to upload and update. The site in question is w w w . m a r p e l y . c o m

3 page

```html
<!DOCTYPE html>
<html lang="en">
<head>
<meta charset="utf-8">
<title>Sales Banners – Page C4</title>
<link href="https://fonts.googleapis.com/css2?family=Montserrat:wght@800;900&family=Poppins:wght@700;800;900&family=Anton&display=swap" rel="stylesheet">
<style>
  :root{
    --page:#ffffff;
    --amber:#f5b50f;
    --amber-deep:#ef9d0c;
    --amber-light:#fbd03a;
    --navy:#141a2b;
    --magenta:#b3188f;
    --magenta-deep:#8d137a;
    --teal:#3ecfd4;
    --plum:#5e0f5d;
    --plum-mid:#7a1468;
    --ochre:#b8921c;
    --sun:#f6c80e;
    --sun-ring:#ffe31a;
    --red:#d6301a;
    --mist:#d2d8e0;
    --lemon:#f5d50c;
    --ink:#111111;
    --white:#ffffff;
  }
  *{margin:0;padding:0;box-sizing:border-box}
  html,body{width:920px;height:1200px;overflow:hidden;background:var(--page)}
  .page{position:relative;width:920px;height:1200px}
  .banner{position:absolute;left:102px;width:717px;height:314px;overflow:hidden}
  .banner svg.art{position:absolute;inset:0;width:100%;height:100%}
  .photo{position:absolute;border-radius:6px}
  .txt{position:absolute;line-height:1;white-space:nowrap}

  /* Banner 1 – Today only */
  .banner--today{top:47px;background:radial-gradient(circle at 68% 50%,var(--amber-light) 0,var(--amber) 45%,var(--amber-deep) 100%)}
  .banner--today .photo{left:358px;top:56px;width:243px;height:216px;background:linear-gradient(180deg,#2a2a2a 0 28%,#f1f1f1 28% 62%,#1b1b1b 62% 100%)}
  .today{font-family:'Montserrat',sans-serif;font-weight:900;color:var(--navy);transform-origin:left center}
  .today-only{left:68px;top:86px;font-size:21px;transform:rotate(-9deg)}
  .today-sale{left:54px;top:128px;font-size:76px;color:var(--white);transform:rotate(-10deg)}
  .today-upto{left:152px;top:213px;font-size:24px;color:var(--white);transform:rotate(-10deg)}
  .today-upto .accent{color:var(--amber)}
  .today-shop{left:208px;top:251px;font-size:14px;transform:rotate(-11deg)}

  /* Banner 2 – Rattan */
  .banner--rattan{top:421px;background:var(--teal)}
  .banner--rattan .photo{left:424px;top:125px;width:279px;height:155px;background:linear-gradient(160deg,#3a3a3a,#151515)}
  .rattan{font-family:'Poppins',sans-serif;font-weight:800}
  .rattan-main{left:51px;width:258px;text-align:center;top:53px;font-size:27px;color:var(--magenta);letter-spacing:-.8px}
  .rattan-sub{left:51px;width:258px;text-align:center;top:80px;font-size:17px;color:var(--white);letter-spacing:-.3px}
  .rattan-get{left:225px;top:144px;font-size:27px;color:var(--white)}
  .rattan-num{left:223px;top:166px;font-size:46px;color:var(--white);letter-spacing:-1px}
  .rattan-off{left:288px;top:180px;font-size:18px;color:var(--white)}
  .rattan-shop{position:absolute;left:225px;top:263px;width:79px;height:25px;border-radius:13px;background:var(--sun);font-family:'Poppins',sans-serif;font-weight:800;font-size:8px;color:var(--plum);display:flex;align-items:center;justify-content:center}

  /* Banner 3 – Divan */
  .banner--divan{top:802px;background:var(--mist)}
  .banner--divan .photo{left:180px;top:43px;width:285px;height:230px;background:linear-gradient(170deg,#f2f2f2 0 40%,#7a5a3c 40% 60%,#e6e6e6 60%)}
  .divan{font-family:'Anton',sans-serif}
  .divan-list{list-style:none}
  .divan-list li{position:absolute;left:29px;line-height:1;white-space:nowrap}
  .divan-list .y{color:var(--lemon);font-size:35px}
  .divan-list .w{color:var(--white);font-size:41px}
  .divan-list .l1{top:61px}
  .divan-list .l2{top:100px}
  .divan-list .l3{top:141px}
  .divan-list .l4{top:177px}
  .divan-list .l5{top:218px}
  .divan-best{left:512px;top:114px;font-size:18px;color:var(--white)}
  .divan-big{left:489px;width:170px;text-align:center;top:153px;font-size:46px;color:var(--ink)}
  .divan-big .accent{color:var(--red)}
  .divan-upto{left:498px;top:240px;font-size:15px;color:var(--white)}
  .divan-upto .accent{color:var(--lemon)}

  .page-mark{position:absolute;left:884px;top:1118px;font-family:'Anton',sans-serif;font-size:12px;color:var(--ink)}
</style>
</head>
<body>
<div class="page">

  <section class="banner banner--today">
    <div class="photo" role="img" aria-label="Photo of a divan bed with black base, white mattress, pillows, throw and bedside lamp"></div>
    <svg class="art" viewBox="0 0 717 314">
      <polygon points="22,128 284,85 272,131 295,174 24,217 48,171" fill="var(--navy)"/>
      <polygon points="39,117 65,117 53,131" fill="var(--amber)"/>
      <polygon points="53,209 88,209 71,232" fill="var(--amber)"/>
      <polygon points="278,101 295,101 283,125" fill="var(--amber)"/>
      <polygon points="283,167 306,167 294,182" fill="var(--amber)"/>
      <polygon points="131,209 309,177 316,219 134,250 143,230" fill="var(--magenta)"/>
      <polygon points="131,209 143,230 134,250" fill="var(--magenta-deep)"/>
    </svg>
    <div class="txt today today-only">TODAY ONLY</div>
    <div class="txt today today-sale">SALE</div>
    <div class="txt today today-upto">UP TO <span class="accent">70%</span></div>
    <div class="txt today today-shop">SHOP NOW</div>
  </section>

  <section class="banner banner--rattan">
    <svg class="art" viewBox="0 0 717 314">
      <path d="M520,0 H717 V140 C690,80 640,20 600,0 Z" fill="var(--plum-mid)"/>
      <path d="M0,185 C60,160 120,160 180,180 C260,210 330,245 420,230 C470,222 480,200 500,195 V314 H0 Z" fill="var(--plum)"/>
      <circle cx="577" cy="235" r="200" fill="none" stroke="var(--sun-ring)" stroke-width="4"/>
      <circle cx="577" cy="235" r="186" fill="var(--sun)"/>
      <line x1="50" y1="180" x2="22" y2="226" stroke="var(--ochre)" stroke-width="28" stroke-linecap="round"/>
      <line x1="130" y1="160" x2="67" y2="255" stroke="var(--sun)" stroke-width="42" stroke-linecap="round"/>
      <line x1="180" y1="171" x2="125" y2="252" stroke="var(--plum-mid)" stroke-width="40" stroke-linecap="round" opacity=".85"/>
      <polygon points="53,30 300,24 304,120 55,124" fill="none" stroke="var(--magenta)" stroke-width="2"/>
      <polygon points="57,34 300,28 302,116 58,120" fill="none" stroke="var(--sun)" stroke-width="2"/>
      <polygon points="59,28 306,42 300,124 50,112" fill="none" stroke="var(--white)" stroke-width="2.5"/>
      <line x1="299" y1="151" x2="277" y2="209" stroke="var(--white)" stroke-width="2"/>
      <circle cx="281" cy="161" r="2.4" fill="none" stroke="var(--white)" stroke-width="1.4"/>
      <circle cx="297" cy="168" r="2.4" fill="none" stroke="var(--white)" stroke-width="1.4"/>
    </svg>
    <div class="photo" role="img" aria-label="Photo of a black rattan dining cube set with cream cushions"></div>
    <div class="txt rattan rattan-main">RATTAN 11 PIECE</div>
    <div class="txt rattan rattan-sub">RECTANGULAR CUBE SET</div>
    <div class="txt rattan rattan-get">GET</div>
    <div class="txt rattan rattan-num">70</div>
    <div class="txt rattan rattan-off">OFF</div>
    <div class="rattan-shop">SHOP NOW</div>
  </section>

  <section class="banner banner--divan">
    <svg class="art" viewBox="0 0 717 314">
      <path d="M519,0 H717 V118 C690,90 660,80 620,78 C560,76 535,60 525,30 Z" fill="var(--lemon)" stroke="var(--white)" stroke-width="3"/>
      <polygon points="0,0 249,0 376,314 0,314" fill="var(--red)"/>
      <g stroke="var(--lemon)" stroke-width="4">
        <line x1="28" y1="16" x2="64" y2="51"/><line x1="40" y1="12" x2="76" y2="47"/><line x1="54" y1="10" x2="96" y2="46"/>
      </g>
      <polygon points="663,115 652,233 543,215" fill="var(--red)"/>
      <g stroke="var(--ink)" stroke-width="4">
        <line x1="610" y1="226" x2="642" y2="253"/><line x1="624" y1="226" x2="656" y2="251"/><line x1="638" y1="228" x2="668" y2="250"/>
      </g>
      <rect x="489" y="150" width="170" height="63" fill="var(--white)"/>
      <polygon points="490,111 597,106 607,141 490,135" fill="var(--ink)"/>
      <polygon points="479,236 593,236 600,248 593,261 486,261 490,248" fill="var(--red)"/>
    </svg>
    <div class="photo" role="img" aria-label="Photo of a white ottoman storage divan bed with the mattress lifted open"></div>
    <svg class="art" viewBox="0 0 717 314">
      <g stroke="var(--lemon)" stroke-width="4">
        <line x1="214" y1="244" x2="250" y2="278"/><line x1="228" y1="239" x2="264" y2="274"/><line x1="244" y1="235" x2="280" y2="268"/>
      </g>
    </svg>
    <ul class="divan divan-list">
      <li class="y l1">OTTOMAN</li>
      <li class="w l2">STORAGE</li>
      <li class="y l3">SIDE LIFT</li>
      <li class="y l4">ESSENTIAL</li>
      <li class="w l5">DIVAN</li>
    </ul>
    <div class="txt divan divan-best">BEST OFFER</div>
    <div class="txt divan divan-big">BIG <span class="accent">SALE</span></div>
    <div class="txt divan divan-upto">UP TO <span class="accent">50%</span> OFF</div>
  </section>

  <div class="page-mark">C4</div>
</div>
</body>
</html>
```